Personal Business Card Design Project

I require a two sided personal business card design.

I am a 35 year old Angel Investor and I invest in various niche internet and F&B projects in China. I am Chinese Australian

One side should be in English and the other side should be in Chinese.

My English details are:

Milo Varden
Angel Investor

China: +86 1703 482 5164
Hong Kong: +852 6437 2189
Email: milo@mvardenmail.com
Address: Flat 2407, Block 6, Birchmoor Terrace,
52 Qiaolan Road (near Fengyu Road),
Shanghai, 200417,
China

My Chinese details are (do not print the text in brackets)

韦朗舟 (Name)
天使投资者(Angel Investor)

中国 (China): +86 1703 482 5164
香港 (Hong Kong): +852 6437 2189
Email: milo@mvardenmail.com
地址 (Address): 上海市桥澜路52号6号楼2407室
枫影华苑, 中国 200417

Target Market(s)

I will only give this card to present to new partners and suppliers and people asking for funding. Not customers.

Industry/Entity Type

Internet

Requirements
Must have
• Something a little humourous in terms of graphics that suggest helping something to grow since I invest in startups. But I want a sophisticated look to it as well.
Nice to have
• Black and White tongue in cheek graphics but not overboard.

The whole card can be not conventional in shape or have cutouts but still retain the business standard business card size.

```html
<!DOCTYPE html>
<html lang="en">
<head>
<meta charset="utf-8">
<title>Milo Varden – Business Card</title>
<link rel="stylesheet" href="https://fonts.googleapis.com/css2?family=Arimo:ital,wght@0,400;0,700;1,700&family=Noto+Serif:wght@400&family=Noto+Serif+SC:wght@400&display=swap">
<style>
:root{
  --stage:#000000;
  --card-white:#ffffff;
  --band-mid:#e3e8f5;
  --band-end:#8ea3d7;
  --ink:#1c1c1c;
  --ink-soft:#444444;
  --call:#4b4b4b;
  --accent-blue:#6f8fd2;
  --stripe-blue:#7690d2;
  --stripe-grey:#a9acb3;
  --stripe-light:#d6d8dc;
  --divider:#8a8a8a;
  --figure-light:#f2f2f2;
  --figure-mid:#c9c9c9;
}
*{margin:0;padding:0;box-sizing:border-box}
html,body{width:1200px;height:1001px;overflow:hidden;background:var(--stage)}
.stage{position:relative;width:1200px;height:1001px}
.card{position:absolute;left:250px;width:700px;height:422px;background:var(--card-white);overflow:hidden}
.card--english{top:55px}
.card--chinese{top:524px}
.chevrons{position:absolute;inset:0;width:700px;height:422px}
.band{position:absolute;left:0;right:0;top:185px;bottom:0;
  background:linear-gradient(to bottom,var(--card-white) 0%,var(--band-mid) 45%,var(--band-end) 100%);
  border-top:1px solid var(--divider)}
.illustration{position:absolute;left:18px;top:12px;width:186px;height:168px;border-radius:6px;
  background:radial-gradient(ellipse at 50% 45%,var(--figure-light) 0%,var(--figure-mid) 70%,var(--card-white) 100%)}
.identity{position:absolute;top:58px;width:300px;margin-left:-150px;text-align:center}
.card--english .identity{left:375px}
.card--chinese .identity{left:365px;top:72px}
.name{font-family:"Noto Serif",serif;font-size:26px;color:var(--ink-soft);font-weight:400}
.title{font-family:Arimo,sans-serif;font-weight:700;font-style:italic;font-size:24px;color:var(--accent-blue);margin-top:2px}
.name--zh{font-family:"Noto Serif SC",serif;font-size:25px}
.title--zh{font-family:"Noto Serif SC",serif;font-weight:400;font-style:normal;font-size:24px;margin-top:6px}
.call,.call-reflection{position:absolute;left:16px;font-family:Arimo,sans-serif;font-weight:700;font-size:50px;color:var(--call);line-height:50px;height:50px;white-space:nowrap}
.call{top:258px}
.call-reflection{top:306px;transform:scaleY(-0.85);transform-origin:50% 0;opacity:.5;
  -webkit-mask-image:linear-gradient(to bottom,transparent 20%,rgba(0,0,0,.9) 90%);
  mask-image:linear-gradient(to bottom,transparent 20%,rgba(0,0,0,.9) 90%)}
.call-reflection{transform:translateY(42px) scaleY(-0.85)}
.contact{position:absolute;right:14px;text-align:right;color:var(--ink);font-family:Arimo,sans-serif;font-size:17px;line-height:21px}
.card--english .contact{top:228px}
.contact b{font-weight:700;font-style:italic}
.contact--zh{top:244px;font-family:"Noto Serif SC",serif;font-size:17px;line-height:21px;color:var(--ink-soft)}
.address-zh{display:flex;justify-content:flex-end;gap:6px;margin-top:8px;text-align:left}
</style>
</head>
<body>
<main class="stage">

  <section class="card card--english" aria-label="English side">
    <div class="band"></div>
    <svg class="chevrons" viewBox="0 0 700 422" aria-hidden="true">
      <polygon points="476,89 600,0 620,0" fill="var(--stripe-blue)"/>
      <polygon points="476,89 620,0 652,0" fill="var(--stripe-grey)"/>
      <polygon points="476,89 652,0 700,0 700,6" fill="var(--stripe-light)"/>
      <polygon points="476,89 555,185 590,185" fill="var(--stripe-blue)"/>
      <polygon points="476,89 590,185 640,185" fill="var(--stripe-grey)"/>
      <polygon points="476,89 640,185 700,185 700,176" fill="var(--stripe-light)"/>
    </svg>
    <div class="illustration" role="img" aria-label="Humorous 3D figures shaking hands, one with angel wings holding a briefcase"></div>
    <div class="identity">
      <p class="name">Milo Varden</p>
      <p class="title">Angel Investor</p>
    </div>
    <p class="call">Call NOW!</p>
    <p class="call-reflection" aria-hidden="true">Call NOW!</p>
    <div class="contact">
      <p><b>China:</b> +86 1703 482 5164</p>
      <p><b>Hong Kong:</b> +852 6437 2189</p>
      <p><b>Email:</b> milo@mvardenmail.com</p>
      <p><b>Address:</b> Flat 2407, Block 6, Birchmoor Terrace</p>
      <p>52 Qiaolan Road (near Fengyu Road)</p>
      <p>Shanghai, 200417</p>
      <p>China</p>
    </div>
  </section>

  <section class="card card--chinese" aria-label="Chinese side" lang="zh">
    <div class="band"></div>
    <svg class="chevrons" viewBox="0 0 700 422" aria-hidden="true">
      <polygon points="476,89 600,0 620,0" fill="var(--stripe-blue)"/>
      <polygon points="476,89 620,0 652,0" fill="var(--stripe-grey)"/>
      <polygon points="476,89 652,0 700,0 700,6" fill="var(--stripe-light)"/>
      <polygon points="476,89 555,185 590,185" fill="var(--stripe-blue)"/>
      <polygon points="476,89 590,185 640,185" fill="var(--stripe-grey)"/>
      <polygon points="476,89 640,185 700,185 700,176" fill="var(--stripe-light)"/>
    </svg>
    <div class="illustration" role="img" aria-label="Humorous 3D figures shaking hands, one with angel wings holding a briefcase"></div>
    <div class="identity">
      <p class="name name--zh">韦朗舟</p>
      <p class="title title--zh">天使投资者</p>
    </div>
    <p class="call" lang="en">Call NOW!</p>
    <p class="call-reflection" aria-hidden="true">Call NOW!</p>
    <div class="contact contact--zh">
      <p>中国：+86 1703 482 5164</p>
      <p>香港：+852 6437 2189</p>
      <p>Email: milo@mvardenmail.com</p>
      <div class="address-zh">
        <span>地址：</span>
        <span>上海市桥澜路52号6号楼2407室<br>枫影华苑, 中国 200417</span>
      </div>
    </div>
  </section>

</main>
</body>
</html>
```